Harborline Open Cinema Gathering 20th Annual Poster

September 2017 will to the 20th Annual Harborline Open Cinema Gathering. We have a new logo and need a new modern stylish poster designed. One that shows creativity, imagination, style and class. Think outside the box. Modern and new.

Dates are: September 7th - 13th 2017

Our tagline:
"Something for Everyone from Around the World"

Target Market(s)

film festival goings - 35 - 70 age range - 58% female 42% males - movie lovers - movie goers

Industry/Entity Type

Movie

Font styles to use
Script

Requirements
Must have
• modern style celebrating 20 years - cool design - chic and stylish - upscale - high society - think Abstract
Nice to have
• thinking outside the box - not just simple film reel - think Abstract! Not just your standard film items. Creative in your idea and design
Should not have
• no CLIP ART

```html
<!DOCTYPE html>
<html lang="en">
<head>
<meta charset="utf-8">
<title>Harborline Open Cinema Gathering – 20th Annual Poster</title>
<link rel="stylesheet" href="https://fonts.googleapis.com/css2?family=Aldrich&display=swap">
<style>
  :root {
    --paper: #ffffff;
    --ink: #151515;
    --white: #ffffff;
    --red: #d8322a;
    --maroon: #3a0a12;
    --ember: #d3442a;
    --violet: #7a4e8a;
    --teal: #5f9f93;
    --sage: #8ec28a;
    --aperture: #2a0614;
    --date-dark: #2a1020;
  }
  * { margin: 0; padding: 0; box-sizing: border-box; }
  html, body { width: 837px; height: 1200px; overflow: hidden; background: var(--paper); }
  .poster {
    position: relative; width: 837px; height: 1200px; background: var(--paper);
    font-family: "Aldrich", sans-serif; text-transform: uppercase;
  }
  .artwork {
    position: absolute; left: 47px; top: 49px; width: 751px; height: 1093px; overflow: hidden;
    background:
      radial-gradient(ellipse 200px 190px at 50% 80%, var(--aperture) 0%, rgba(42,6,20,0.9) 60%, rgba(42,6,20,0) 100%),
      radial-gradient(ellipse 420px 320px at 30% 38%, rgba(211,68,42,0.85) 0%, rgba(211,68,42,0) 100%),
      radial-gradient(ellipse 500px 420px at 80% 90%, rgba(142,194,138,0.85) 0%, rgba(142,194,138,0) 100%),
      linear-gradient(175deg, var(--maroon) 0%, #6a1a22 22%, var(--violet) 52%, var(--teal) 78%, var(--sage) 100%);
  }
  .headline { position: absolute; left: 0; width: 100%; text-align: center; line-height: 1; }
  .edition { top: 48px; font-size: 54px; color: var(--red); letter-spacing: 4px; }
  .event-name { top: 112px; font-size: 44px; color: var(--white); letter-spacing: 3px; line-height: 62px; }
  .dates { position: absolute; left: 0; width: 100%; text-align: center; line-height: 1; }
  .month { top: 368px; font-size: 34px; color: var(--white); letter-spacing: 1px; }
  .days { top: 414px; font-size: 32px; color: var(--date-dark); letter-spacing: 1px; }
  .year { top: 458px; font-size: 96px; color: var(--white); }
  .brand {
    position: absolute; left: 0; width: 100%; top: 835px; text-align: center; color: var(--white);
  }
  .brand-dot { width: 58px; height: 58px; border-radius: 50%; background: var(--sage); margin: 0 auto 18px; }
  .brand-name { font-size: 30px; line-height: 38px; letter-spacing: 2px; }
  .tagline {
    position: absolute; left: 47px; width: 751px; top: 1164px; font-size: 17px; color: var(--ink);
    display: flex; justify-content: space-between; letter-spacing: 0;
  }
</style>
</head>
<body>
  <main class="poster">
    <div class="artwork" role="img" aria-label="Close-up photograph of a camera lens aperture with brushed-metal blades glowing red, violet and teal around a dark hexagonal opening">
      <h1 class="headline edition">20th Annual</h1>
      <h2 class="headline event-name">Harborline Open Cinema<br>Gathering</h2>
      <p class="dates month">September</p>
      <p class="dates days">7th – 13th</p>
      <p class="dates year">2017</p>
      <div class="brand">
        <div class="brand-dot"></div>
        <p class="brand-name">Harborline<br>Open Cinema Gathering</p>
      </div>
    </div>
    <p class="tagline">
      <span>S</span><span>o</span><span>m</span><span>e</span><span>t</span><span>h</span><span>i</span><span>n</span><span>g</span><span>&nbsp;</span>
      <span>f</span><span>o</span><span>r</span><span>&nbsp;</span>
      <span>e</span><span>v</span><span>e</span><span>r</span><span>y</span><span>o</span><span>n</span><span>e</span><span>&nbsp;</span>
      <span>f</span><span>r</span><span>o</span><span>m</span><span>&nbsp;</span>
      <span>a</span><span>r</span><span>o</span><span>u</span><span>n</span><span>d</span><span>&nbsp;</span>
      <span>t</span><span>h</span><span>e</span><span>&nbsp;</span>
      <span>w</span><span>o</span><span>r</span><span>l</span><span>d</span>
    </p>
  </main>
</body>
</html>
```